Meridane Works, Inc. - Update our Website

Meridane Works needs a website to help our customers to navigate through our services efficiently. Our existing website is at www.meridwork.example

We would like to explain our services with content and pictures (photographs) that distinguishes our products and services from our competition.

The website design must implement a strategy to focus on our Contract Labeling services.

With this new design we would like to attract new customers and ensure that our existing customers are fully informed with our latest offerings.

```html
<!DOCTYPE html>
<html lang="en">
<head>
<meta charset="utf-8">
<title>Meridane Works, Inc.</title>
<link href="https://fonts.googleapis.com/css2?family=Barlow:wght@400;500;600;700&display=swap" rel="stylesheet">
<style>
:root{
  --blue:#1a7bb9;
  --blue-dark:#0f6fa8;
  --footer:#0b7dbd;
  --green:#7dc81e;
  --text:#444;
  --line:#cfcfcf;
  --white:#fff;
}
*{margin:0;padding:0;box-sizing:border-box}
html,body{width:845px;height:1200px;overflow:hidden;background:var(--white)}
body{font-family:"Barlow",Arial,sans-serif;color:var(--text)}
.page{position:relative;width:1000px;height:1420px;transform:scale(.845);transform-origin:0 0}
.abs{position:absolute}
.btn{position:absolute;background:var(--blue);color:var(--white);font-weight:600;display:flex;align-items:center;justify-content:center;letter-spacing:.3px}

/* header */
.brand{left:25px;top:20px;display:flex;align-items:center;gap:10px}
.brand-dot{width:40px;height:40px;border-radius:50%;background:var(--green)}
.brand-name{font-weight:700;font-size:18px;color:#222;line-height:1;letter-spacing:.5px}
.nav{left:326px;top:34px;display:flex;font-size:13px;font-weight:600;color:var(--blue);letter-spacing:.3px}
.nav span.sep{margin:0 14px}
.rule-green{left:0;width:1000px;height:4px;background:var(--green)}

/* hero */
.hero{left:0;top:74px;width:1000px;height:308px;background:linear-gradient(100deg,#f4f4f4 0%,#ececec 45%,#d9d9d9 70%,#f0f0f0 100%)}
.hero-title{left:73px;top:142px;font-size:35px;font-weight:700;color:var(--blue);line-height:34px;letter-spacing:.2px}
.hero-copy{left:73px;top:217px;width:440px;font-size:12.5px;font-weight:600;line-height:21px;color:#555}
.dots{left:725px;top:331px;display:flex;gap:16px}
.dots i{width:14px;height:14px;border-radius:50%;border:2px solid var(--blue);background:var(--white);display:block}
.dots i.on{background:radial-gradient(circle,var(--green) 0 3px,var(--white) 3.5px)}

/* welcome */
.welcome-title{left:0;top:420px;width:1000px;text-align:center;font-size:34px;font-weight:700;color:var(--blue);line-height:34px}
.welcome-copy{left:40px;top:497px;width:920px;text-align:center;font-size:12.5px;line-height:13.5px;color:#444}

/* feature */
.feature-title{left:39px;top:562px;font-size:25px;font-weight:700;color:var(--blue)}
.feature-sub{left:39px;top:591px;width:563px;display:flex;align-items:center;font-size:16px;font-weight:600;color:var(--blue)}
.feature-sub::after{content:"";flex:1;height:1px;background:var(--line);margin-left:4px}
.feature-copy{left:41px;top:621px;width:565px;font-size:12.5px;line-height:16.6px;color:#444}
.feature-rule{left:39px;top:754px;width:563px;height:1px;background:var(--line)}
.feature-photo{left:625px;top:601px;width:333px;height:153px;border:2px solid #ddd;background:linear-gradient(120deg,#6d6d6d,#b9b9b9 45%,#e6e6e6 70%,#9a9a9a)}

/* cards */
.card-bar{top:809px;height:5px;background:var(--blue-dark)}
.card{top:829px;width:298px;height:293px;border:2px solid #dedede;background:var(--white)}
.card-photo{position:absolute;left:0;top:0;width:100%;height:121px}
.card-head{position:absolute;left:0;top:121px;width:100%;height:33px;background:var(--green);color:var(--white);font-size:16px;font-weight:700;padding-left:22px;line-height:33px;letter-spacing:.3px}
.card-copy{position:absolute;left:24px;top:174px;width:250px;font-size:12.5px;line-height:12.6px;color:#444}
.card .btn{left:160px;top:251px;width:113px;height:26px;font-size:12.5px}

/* footer */
.footer{left:0;top:1160px;width:1000px;height:260px;background:var(--footer);color:var(--white)}
.f-title{position:absolute;font-size:22px;font-weight:700;top:55px;letter-spacing:.3px}
.f-text{position:absolute;font-size:12.5px;font-weight:600;line-height:21px}
.f-div{position:absolute;top:37px;width:1px;height:203px;background:rgba(255,255,255,.35)}
.f-row{display:flex}
.f-row b{font-weight:600;width:72px}
.social{position:absolute;left:480px;top:201px;display:flex;gap:16px}
.social i{display:block;width:24px;height:24px;border-radius:50%;border:2px solid var(--white)}
.signup{position:absolute;left:750px;top:147px;width:205px;height:34px;display:flex;border:2px solid #0a5f91}
.signup .field{flex:1;background:var(--white);color:#8aa;font-size:12px;letter-spacing:.8px;display:flex;align-items:center;padding-left:7px}
.signup .submit{width:72px;background:var(--footer);font-size:12.5px;font-weight:700;display:flex;align-items:center;justify-content:center}
</style>
</head>
<body>
<div class="page">

  <header>
    <div class="abs brand"><span class="brand-dot"></span><span class="brand-name">MERIDANE WORKS INC.</span></div>
    <nav class="abs nav">
      <span>HOME</span><span class="sep">|</span><span>ABOUT US</span><span class="sep">|</span><span>OUR SERVICES</span><span class="sep">|</span><span>OUR PRODUCTS</span><span class="sep">|</span><span>USER SUPPORT</span><span class="sep">|</span><span>CONTACT YS</span>
    </nav>
  </header>

  <div class="abs rule-green" style="top:70px"></div>
  <section class="abs hero" role="img" aria-label="Gloved hands holding a medicine vial and a printed clinical label"></section>
  <div class="abs rule-green" style="top:382px"></div>
  <h1 class="abs hero-title">WITH CLINICAL LABEL STOCK<br>MY JOB HAS BECOME EASIER!</h1>
  <p class="abs hero-copy">MeriStock™ is a premium line of label stock products that Meridane Works supplies to the pharmaceutical industry. These label STOCKS are specifically designed for use by clinical supply departments for the computer printing of clinical study labels.</p>
  <div class="btn" style="left:75px;top:306px;width:119px;height:35px;font-size:17px">READ MORE</div>
  <div class="abs dots"><i class="on"></i><i></i><i></i></div>

  <h2 class="abs welcome-title">WELCOME TO<br>MERIDANE WORKS, INC OFFICAL WEBSITE</h2>
  <p class="abs welcome-copy">Meridane Works, Inc. SPECIALIZES in providing products and services to the pharmaceutical industry. We are focused on the needs of those individuals involved with Clinical Trial Materials. Our products and services are summarized below, to know more about our company</p>
  <div class="btn" style="left:455px;top:533px;width:91px;height:27px;font-size:12.5px">READ MORE</div>

  <h3 class="abs feature-title">MERISTOCK™</h3>
  <div class="abs feature-sub">CLINICAL LABEL STOCK</div>
  <p class="abs feature-copy">MeriStock™ is a premium line of label stock products that Meridane Works supplies to the pharmaceutical industry. These label STOCKS are specifically designed for use by clinical supply departments for the computer printing of clinical study labels. Labels are available from our in-house inventories or converted for you on a custom basis. This allows you to obtain the correct combination of size and structural configuration with the appropriate facesheet, ink, adhesive and liner material for your REQUIREMENTS. Labels can be finished in fanfolds, rolls or sheets for use with a wide variety of computer printer technologies.</p>
  <div class="abs feature-rule"></div>
  <div class="abs feature-photo" role="img" aria-label="Gloved hands loading a label roll into a label printer beside a keyboard"></div>

  <div class="abs card-bar" style="left:36px;width:300px"></div>
  <div class="abs card-bar" style="left:352px;width:300px"></div>
  <div class="abs card-bar" style="left:666px;width:300px"></div>

  <article class="abs card" style="left:37px">
    <div class="card-photo" role="img" aria-label="Hands holding a vial over printed label sheets" style="background:linear-gradient(110deg,#f2f2f2,#d8d8d8 55%,#c4b6a8)"></div>
    <div class="card-head">MERISERV™</div>
    <p class="card-copy">MeriServ™ is a contract clinical label generation service that provides you with ready to APPLY clinical labels specifically designed and produced for your clinical trial needs.</p>
    <div class="btn">READ MORE</div>
  </article>

  <article class="abs card" style="left:349px">
    <div class="card-photo" role="img" aria-label="Gloved lab hands working with test tubes and colorful sample vials" style="background:linear-gradient(180deg,#9fd1c8,#cfe4e6 45%,#8aa0b8 80%,#b05a6a)"></div>
    <div class="card-head">MERIBOOK™</div>
    <p class="card-copy">MeriServ™ is a contract clinical label generation service that provides you with ready to APPLY clinical labels specifically designed and produced for your clinical trial needs.</p>
    <div class="btn">READ MORE</div>
  </article>

  <article class="abs card" style="left:667px">
    <div class="card-photo" role="img" aria-label="Doctor in a white coat with a stethoscope standing in a clinic" style="background:linear-gradient(90deg,#e3e6ea,#f3f3f3 35%,#dfe3e8 60%,#eef0f2)"></div>
    <div class="card-head">CLINICAL RANDOMIZATIONS</div>
    <p class="card-copy">MeriServ™ is a contract clinical label generation service that provides you with ready to APPLY clinical labels specifically designed and produced for your clinical trial needs.</p>
    <div class="btn">READ MORE</div>
  </article>

  <footer class="abs footer">
    <h4 class="f-title" style="left:40px">OFFICES AND LOCATIONS</h4>
    <div class="f-text" style="left:40px;top:82px">
      412 ALDER STREET<br>BROOKHAVEN<br>NY 11590 USA
      <div class="f-row"><b>PHONE:</b>+1-555-210-4400</div>
      <div class="f-row"><b>FAX:</b>+1-555-210-4401</div>
    </div>
    <div class="f-text" style="left:240px;top:82px">
      238 FENWICK STREET<br>ASHFORD<br>NJ 08599 USA
      <div class="f-row"><b>PHONE:</b>+1-555-380-7700</div>
      <div class="f-row"><b>FAX:</b>+1-555-380-7701</div>
    </div>
    <div class="f-div" style="left:441px"></div>

    <h4 class="f-title" style="left:480px">DIRECT CONTACT</h4>
    <div class="f-text" style="left:480px;top:84px;line-height:17px">Lorem ipsuCum sociis natoque<br>penatibus et magnis dis parturient</div>
    <div class="f-text" style="left:480px;top:132px">(555) 0123&nbsp; 456789</div>
    <div class="f-text" style="left:480px;top:165px">info@meridwork.example</div>
    <div class="social" aria-label="Social links"><i></i><i></i><i></i></div>
    <div class="f-div" style="left:706px"></div>

    <h4 class="f-title" style="left:750px">NEWSLETTER</h4>
    <div class="f-text" style="left:750px;top:82px">Join our mailing list and stay tuned<br>to our latest news.</div>
    <div class="signup"><span class="field">MAIL@DOMAIN.COM</span><span class="submit">SUBMIT</span></div>
    <div class="f-text" style="left:750px;top:204px">All rights reserved . 2014</div>
  </footer>

</div>
</body>
</html>
```